VORKEL COMPOSITES INC website in USA

VORKEL COMPOSITES INC incorporated and operated in USA needs a completely new design of website. This Wyoming based company is a importer and distributor of composites material to supply mainly to American and Canadian/Mexican customers. Our main products includes Carbon Fiber, Aramid Fiber, Glass Fiber, Basalt Fiber, High Silica Glass, Quartz Fiber, S-Glass, Alumina Fiber, Vacuum Auxiliary.

We are one stop composites solution provider for Automotive, Aerospace, Construction, Electrical and Machinery industries.

We are exclusive sales company in North America for DORAQ composites produced from China and their other Asia facilities.

Target Market(s)

USA and Canada

Industry/Entity Type

Composites materials

Coding

Coded - Design and coding required

Number of Pages Required

5+ page

Requirements
Nice to have
• Color theme to match our corporate logo VORKEL. VORKEL stands for Vantor Omniline Reliant Kinetic Export Lodge

```html
<!DOCTYPE html>
<html lang="en">
<head>
<meta charset="utf-8">
<title>VORKEL COMPOSITES INC — Advanced Composites</title>
<link href="https://fonts.googleapis.com/css2?family=Barlow+Condensed:ital,wght@1,700;1,800&family=Poppins:wght@400;500;600&display=swap" rel="stylesheet">
<style>
:root{
  --orange:#f7a01c;
  --orange-deep:#e98b0c;
  --dark:#1d1d1d;
  --dark-2:#2b2b2b;
  --cream:#fbf6ec;
  --text:#3a3a3a;
  --muted:#6d6d6d;
  --white:#ffffff;
  --photo-hero:#2f3442;
}
*{box-sizing:border-box;margin:0;padding:0}
html,body{width:1200px;height:4796px;overflow:hidden}
body{font-family:"Poppins",sans-serif;color:var(--text);background:var(--cream);position:relative}
.abs{position:absolute}
.display{font-family:"Barlow Condensed",sans-serif;font-style:italic;font-weight:800;text-transform:uppercase;letter-spacing:.5px}
.section{position:absolute;left:0;width:1200px}
.center{text-align:center}
.eyebrow{font-size:12px;letter-spacing:.5px;text-transform:uppercase;display:inline-flex;align-items:center;gap:8px}
.eyebrow::before{content:"";width:28px;height:28px;border-left:2px solid currentColor;border-top:2px solid currentColor;border-radius:50% 0 0 0;opacity:.7}
.section-title{font-size:34px;color:var(--dark)}
.lead{font-size:12.5px;line-height:21px;color:var(--text)}
.btn{display:inline-flex;align-items:center;height:34px;border-radius:6px;font-size:11px;font-weight:500;padding:0 46px 0 18px;position:relative;white-space:nowrap}
.btn::after{content:"→";position:absolute;right:0;top:-2px;width:34px;height:38px;border:2px solid currentColor;border-left:none;border-radius:0 50% 50% 0;display:flex;align-items:center;justify-content:center;font-size:15px}
.btn-orange{background:var(--orange);color:var(--white)}
.btn-orange::after{color:var(--orange-deep)}
.btn-ghost{border:1.5px solid var(--white);color:var(--white)}
.btn-light{background:var(--white);color:var(--dark)}
.btn-light::after{color:var(--white)}

.logo{display:flex;align-items:center;gap:10px;color:var(--white)}
.logo-mark{width:16px;height:16px;background:var(--orange);border-radius:50%}
.logo-name{font-size:26px;font-weight:600;letter-spacing:1px}
.logo-sub{font-size:8px;line-height:10px;width:90px;border-left:1px solid #999;padding-left:8px}
.nav{left:320px;top:22px;width:596px;height:36px;background:#c9c9c9;border-radius:20px;display:flex;align-items:center;gap:22px;padding:0 24px;font-size:12px;color:#333}
.nav .active{background:var(--white);color:var(--orange);padding:4px 14px;border-radius:14px}

.hero-title{left:63px;top:158px;font-size:58px;line-height:62px;color:var(--white)}
.hero-title span{color:var(--orange)}
.hero-copy{left:63px;top:372px;width:500px;font-size:11.5px;line-height:20px;color:#e4e4e4}

.product{position:absolute;top:958px;width:242px;height:242px;border-radius:50%;border:4px solid var(--orange);overflow:hidden}
.product .label{position:absolute;bottom:30px;width:100%;text-align:center;color:var(--white);font-size:19px;font-weight:500}
.product .label::after{content:"⌄";display:block;font-size:12px;line-height:8px}
.arrow-round{width:40px;height:40px;border-radius:50%;border:2px solid var(--orange);display:flex;align-items:center;justify-content:center;color:var(--orange);font-size:16px}

.industry{position:absolute;top:1655px;width:180px;text-align:center;color:var(--white)}
.industry .ico{width:84px;height:84px;border-radius:50%;background:var(--white);margin:0 auto 18px;display:flex;align-items:center;justify-content:center}
.industry h3{font-size:22px;font-weight:500;margin-bottom:10px}
.industry p{font-size:13px;line-height:20px}

.bullets{list-style:none;font-size:12px;line-height:23.5px}
.bullets li::before{content:"•";margin-right:10px}

.why-item{position:absolute;left:555px;display:flex;gap:28px;width:500px}
.why-item .ico{width:46px;height:46px;background:var(--dark);border-radius:4px;flex:none;display:flex;align-items:center;justify-content:center}
.why-item h4{font-size:12px;font-weight:600;color:var(--white);margin:4px 0 6px}
.why-item p{font-size:8.5px;line-height:13px;color:#fff6e6}

.card{position:absolute;overflow:hidden;border-radius:4px}
.card .tag{position:absolute;top:14px;right:14px;background:var(--dark);color:var(--white);font-size:10px;padding:4px 12px}
.card .foot{position:absolute;left:0;bottom:0;width:100%;height:66px;background:var(--orange);color:var(--white);padding:12px 20px;font-size:12px;line-height:21px}
.card .foot em{font-style:normal;font-size:10px;position:absolute;right:40px;bottom:12px}

.foot-col h5{font-size:12px;font-weight:600;color:var(--dark);margin-bottom:18px;text-transform:uppercase}
.foot-col li{list-style:none;font-size:10px;line-height:20px;color:var(--muted)}
</style>
</head>
<body>

<!-- HERO -->
<section class="section" style="top:0;height:720px">
  <svg class="abs" style="left:0;top:0" width="1200" height="720" viewBox="0 0 1200 720">
    <defs>
      <linearGradient id="heroDark" x1="0" y1="0" x2="1" y2="1">
        <stop offset="0" stop-color="#2a2a2a"/><stop offset="1" stop-color="#141414"/>
      </linearGradient>
    </defs>
    <path d="M0 0H1200V700C1000 700 820 640 560 600C330 565 150 560 0 520Z" fill="url(#heroDark)"/>
    <path d="M0 528C150 568 330 575 560 610C820 650 1000 708 1200 710" fill="none" stroke="var(--orange)" stroke-width="8"/>
  </svg>
  <div class="abs" role="img" aria-label="Photo: technician presenting a rolled composite sheet"
       style="left:680px;top:90px;width:360px;height:580px;border-radius:8px;background:linear-gradient(180deg,#3a3e48,var(--photo-hero))"></div>

  <div class="abs logo" style="left:55px;top:20px">
    <span class="logo-mark"></span><span class="logo-name">VORKEL</span>
    <span class="logo-sub">Vantor Omniline Reliant Kinetic Export Lodge</span>
  </div>
  <nav class="abs nav">
    <span class="active">Home</span><span>Our Products</span><span>Our Services</span><span>About Us</span><span>Blogs</span><span>Contact Us</span>
  </nav>
  <a class="abs btn btn-orange" style="left:995px;top:25px">Request a Quote</a>

  <h1 class="abs display hero-title">Advanced Composites<br>For Innovative<br><span>Industries</span></h1>
  <p class="abs hero-copy">Your trusted North American partner for Carbon, Aramid, Glass, Basalt, and High-Performance Fibers. Exclusive distributor of DORAQ Composites from China and other Asian facilities.</p>
  <a class="abs btn btn-orange" style="left:63px;top:458px">Explore Products</a>
  <a class="abs btn btn-ghost" style="left:227px;top:458px">Contact Us</a>
</section>

<!-- PRODUCTS -->
<section class="section" style="top:720px;height:698px">
  <div class="abs center" style="left:0;width:1200px;top:52px"><span class="eyebrow" style="color:#444">Product Showcase</span></div>
  <h2 class="abs display section-title center" style="left:0;width:1200px;top:106px">Explore Our High-Performance Materials</h2>
  <p class="abs lead center" style="left:0;width:1200px;top:165px">VORKEL delivers a wide range of advanced fibers and composites<br>engineered for strength, endurance, and precision across industrial sectors.</p>
</section>
<div class="product" role="img" aria-label="Black carbon fiber weave roll" style="left:58px;background:radial-gradient(circle at 40% 40%,#555,#111)"><div class="label">Carbon Fiber</div></div>
<div class="product" role="img" aria-label="Golden aramid fiber twill weave" style="left:340px;background:linear-gradient(135deg,#f0a83a,#a25e0a)"><div class="label">Aramid Fiber</div></div>
<div class="product" role="img" aria-label="Blue glass fiber sheet" style="left:617px;background:radial-gradient(circle at 60% 40%,#4a9ad8,#0b2b55)"><div class="label">Glass Fiber</div></div>
<div class="product" role="img" aria-label="Dark basalt fiber fabric" style="left:895px;background:radial-gradient(circle at 50% 40%,#6a6a6a,#151515)"><div class="label">Basalt Fiber</div></div>
<div class="abs" style="left:342px;top:1172px;width:240px;height:148px;background:var(--dark-2);color:var(--white);padding:62px 18px 0">
  <p style="font-size:10px;text-align:center;margin-bottom:10px">Heat and impact resistant</p>
  <p style="font-size:9px;line-height:13px;text-align:center;color:#bbb">Strong, heat-resistant fiber for protective, aerospace, and industrial use.</p>
  <p style="font-size:9px;color:var(--orange);margin-top:8px">Read More ›</p>
</div>
<div class="abs arrow-round" style="left:1038px;top:1280px">←</div>
<div class="abs arrow-round" style="left:1090px;top:1280px;background:var(--orange);color:var(--white)">→</div>
<a class="abs btn btn-orange" style="left:523px;top:1352px">View All Products</a>

<!-- INDUSTRIES -->
<section class="section" style="top:1418px;height:600px">
  <svg class="abs" style="left:0;top:0" width="1200" height="600" viewBox="0 0 1200 600">
    <defs><linearGradient id="brown" x1="0" y1="0" x2="1" y2="0.4"><stop offset="0" stop-color="#6b430a"/><stop offset=".5" stop-color="#b0720f"/><stop offset="1" stop-color="#e7971a"/></linearGradient></defs>
    <path d="M0 0H1200V560C900 540 600 545 300 575C180 587 80 592 0 595Z" fill="url(#brown)"/>
    <path d="M0 600C200 560 500 540 800 545C950 547 1100 555 1200 565V600Z" fill="var(--orange)"/>
  </svg>
  <div class="abs center" style="left:0;width:1200px;top:48px"><span class="eyebrow" style="color:#fff">Industrial Services</span></div>
  <h2 class="abs display section-title center" style="left:0;width:1200px;top:112px;color:#fff">Engineered for Every Challenge</h2>
  <p class="abs lead center" style="left:0;width:1200px;top:166px;color:#fff">VORKEL materials empower innovation across industries — helping<br>manufacturers design lighter, stronger, and more sustainable solutions.</p>
</section>
<div class="industry" style="left:81px"><div class="ico"><svg width="40" height="40" viewBox="0 0 24 24" fill="var(--orange)"><path d="M5 11l2-5h10l2 5h1v6h-2v2h-3v-2H9v2H6v-2H4v-6zM7.5 11h9l-1.2-3H8.7zM7 13a1.3 1.3 0 100 2.6A1.3 1.3 0 007 13zm10 0a1.3 1.3 0 100 2.6 1.3 1.3 0 000-2.6z"/></svg></div><h3>Automotive</h3><p>Lightweight solutions for performance &amp; safety</p></div>
<div class="industry" style="left:296px"><div class="ico"><svg width="40" height="40" viewBox="0 0 24 24" fill="var(--orange)"><path d="M21 16v-2l-8-5V3.5a1.5 1.5 0 00-3 0V9l-8 5v2l8-2.5V19l-2 1.5V22l3.5-1 3.5 1v-1.5L13 19v-5.5z"/></svg></div><h3>Aerospace</h3><p>Precision materials for flight and structure</p></div>
<div class="industry" style="left:514px"><div class="ico"><svg width="40" height="40" viewBox="0 0 24 24" fill="var(--orange)"><path d="M12 3l9 8h-3v9H6v-9H3zM9 14v6h6v-6z"/></svg></div><h3>Construction</h3><p>Strength and stability for modern builds</p></div>
<div class="industry" style="left:731px"><div class="ico"><svg width="40" height="40" viewBox="0 0 24 24" fill="none" stroke="var(--orange)" stroke-width="2"><circle cx="12" cy="12" r="9"/><path d="M13 5l-5 8h4l-1 6 5-8h-4z" fill="var(--orange)"/></svg></div><h3>Electrical</h3><p>Insulating fibers for energy systems</p></div>
<div class="industry" style="left:948px"><div class="ico"><svg width="40" height="40" viewBox="0 0 24 24" fill="var(--orange)"><path d="M10.5 2h3l.5 2.5 2 1 2.3-1.3 2.1 2.1-1.3 2.3 1 2 2.4.4v3l-2.4.5-1 2 1.3 2.3-2.1 2.1-2.3-1.3-2 1-.5 2.4h-3l-.5-2.4-2-1-2.3 1.3-2.1-2.1 1.3-2.3-1-2L2 13.5v-3l2.5-.5 1-2-1.3-2.3 2.1-2.1 2.3 1.3 2-1zM12 8.5a3.5 3.5 0 100 7 3.5 3.5 0 000-7z"/></svg></div><h3>Machinery</h3><p>Durable materials for industrial equipment</p></div>
<a class="abs btn btn-light" style="left:510px;top:1860px">Explore Our Industry</a>

<!-- ABOUT -->
<section class="section" style="top:2018px;height:600px">
  <div class="abs" style="left:78px;top:40px"><span class="eyebrow" style="color:#444">About VORKEL</span></div>
  <h2 class="abs display section-title" style="left:78px;top:90px;line-height:40px">Delivering Strength<br>Through Innovation</h2>
  <div class="abs lead" style="left:78px;top:186px;width:540px;font-size:12px;line-height:23.5px">
    <p>Headquartered in Wyoming, VORKEL INC is a North American importer and distributor of advanced composite materials.</p>
    <p>&nbsp;We partner with trusted global manufacturers to provide high-quality fibers and accessories to industries that demand reliability and performance.</p>
    <p>&nbsp;Our team combines technical knowledge, responsive service, and global sourcing expertise to help clients build better, stronger products.</p>
  </div>
  <h3 class="abs display" style="left:78px;top:356px;font-size:18px;color:var(--orange)">What Sets VORKEL Apart ?</h3>
  <ul class="abs bullets" style="left:84px;top:390px">
    <li>Complete Solutions: From fibers to vacuum accessories, all in one place</li>
    <li>Uncompromised Quality: Premium materials from audited suppliers</li>
    <li>Global Network, Local Service: International sourcing with regional support</li>
    <li>Innovation Partner: Collaborating to advance your engineering goals</li>
  </ul>
  <a class="abs btn btn-orange" style="left:78px;top:516px">Learn More</a>
  <div class="abs" style="left:700px;top:108px;width:420px;height:420px;border-left:6px solid var(--orange);border-bottom:6px solid var(--orange);border-radius:0 0 0 10px"></div>
  <div class="abs" role="img" aria-label="Hands trimming a dark carbon fiber sheet on a workbench"
       style="left:707px;top:115px;width:409px;height:408px;border-radius:8px;background:linear-gradient(160deg,#5a4a3a,#2a2a2a 60%,#1a1a1a)"></div>
  <div class="abs" style="left:645px;top:82px;width:116px;height:116px;border-radius:50%;background:var(--orange);display:flex;align-items:center;justify-content:center">
    <div style="width:66px;height:66px;border-radius:50%;background:var(--cream)"></div>
  </div>
</section>

<!-- WHY CHOOSE -->
<section class="section" style="top:2618px;height:650px">
  <div class="abs center" style="left:0;width:1200px;top:24px"><span class="eyebrow" style="color:#444">Why Choose Us</span></div>
  <h2 class="abs display section-title center" style="left:0;width:1200px;top:76px">Our Reliable Composite Partner</h2>
  <div class="abs" style="left:480px;top:174px;width:636px;height:334px;background:linear-gradient(90deg,#f7a01c,#fbad2c);border-radius:8px"></div>
  <div class="abs" role="img" aria-label="Warehouse worker beside shelves of stacked composite fabric rolls"
       style="left:-60px;top:100px;width:530px;height:530px;border-radius:50%;border:6px solid var(--orange);background:linear-gradient(140deg,#8a8f96,#3c4046 55%,#c24a2a)"></div>
  <a class="abs btn btn-orange" style="left:530px;top:540px">Request a Quote</a>
</section>
<div class="why-item" style="top:2820px"><div class="ico"><svg width="22" height="22" viewBox="0 0 24 24" fill="none" stroke="#fff" stroke-width="2"><circle cx="12" cy="12" r="3"/><path d="M12 2v5M12 17v5M2 12h5M17 12h5"/></svg></div><div><h4>Direct Importer &amp; Distributor</h4><p>We source high-grade composites directly from trusted global manufacturers, ensuring premium quality and cost efficiency.</p></div></div>
<div class="why-item" style="top:2895px"><div class="ico"><svg width="22" height="22" viewBox="0 0 24 24" fill="none" stroke="#fff" stroke-width="2"><circle cx="12" cy="12" r="8"/><circle cx="12" cy="12" r="3"/></svg></div><div><h4>Multi-Industry Expertise</h4><p>Serving diverse sectors across North America, including automotive, aerospace, construction, and electrical applications.</p></div></div>
<div class="why-item" style="top:2975px"><div class="ico"><svg width="22" height="22" viewBox="0 0 24 24" fill="#fff"><circle cx="12" cy="7" r="3"/><circle cx="5" cy="10" r="2"/><circle cx="19" cy="10" r="2"/><path d="M6 20c0-4 3-7 6-7s6 3 6 7z"/></svg></div><div><h4>Experienced Technical Team</h4><p>Our specialists provide expert guidance, material selection advice, and full logistics support for seamless operations.</p></div></div>
<div class="why-item" style="top:3048px"><div class="ico"><svg width="22" height="22" viewBox="0 0 24 24" fill="none" stroke="#fff" stroke-width="2"><circle cx="12" cy="12" r="9"/><path d="M8 12l3 3 5-6"/></svg></div><div><h4>Consistent Quality &amp; Reliability</h4><p>Every product meets strict performance standards, with dependable supply and on-time delivery you can count on.</p></div></div>

<!-- BLOGS -->
<section class="section" style="top:3268px;height:780px;background:linear-gradient(180deg,var(--cream),#fde8c4)">
  <div class="abs center" style="left:0;width:1200px;top:20px"><span class="eyebrow" style="color:#444">Articles &amp; Blogs</span></div>
  <h2 class="abs display section-title center" style="left:0;width:1200px;top:76px">From the World of Composites</h2>
  <p class="abs lead center" style="left:0;width:1200px;top:134px">Stay up to date on material innovations, market trends, and insights<br>shaping the future of composites and advanced engineering.</p>
</section>
<div class="card" style="left:78px;top:3493px;width:316px;height:394px">
  <div role="img" aria-label="Gloved hands handling grey composite fabric" style="width:100%;height:100%;background:linear-gradient(160deg,#9aa0a8,#4a4f56)"></div>
  <span class="tag">Trending</span>
  <div class="foot">Next-Gen Carbon Fiber in Automotive<br>Engineering<em>Read More »</em></div>
</div>
<div class="card" style="left:418px;top:3486px;width:358px;height:448px">
  <div role="img" aria-label="Hands marking a sheet of red composite fabric" style="width:100%;height:100%;background:linear-gradient(170deg,#6a5a5a,#a04a3a 60%,#3a2a2a)"></div>
  <span class="tag" style="background:#fff;color:#222">Latest News</span>
  <div class="abs" style="left:16px;top:300px;width:326px;height:130px;background:rgba(70,55,50,.8);border-radius:4px;color:#fff;text-align:center;padding:14px 20px">
    <p style="font-size:12px;line-height:20px;color:var(--orange)">VORKEL: Connecting Global Supply with North American Industry</p>
    <p style="font-size:9.5px;line-height:15px;margin-top:10px">Learn how VORKEL ensures reliability and quality in every shipment.</p>
    <p style="font-size:9.5px;color:var(--orange);margin-top:6px">Read More »</p>
  </div>
</div>
<div class="card" style="left:800px;top:3493px;width:316px;height:394px">
  <div role="img" aria-label="Finger touching a perforated composite mesh" style="width:100%;height:100%;background:linear-gradient(160deg,#e6c3a8,#5a5a5a 60%,#222)"></div>
  <span class="tag">Trending</span>
  <div class="foot">Sustainable Composites for a Changing<br>World<em>Read More »</em></div>
</div>
<div class="abs arrow-round" style="left:58px;top:3672px;background:#fff">←</div>
<div class="abs arrow-round" style="left:1096px;top:3672px;background:var(--orange);color:#fff">→</div>
<a class="abs btn btn-orange" style="left:513px;top:3964px">View All Articles</a>

<!-- CTA -->
<section class="section" style="top:4040px;height:330px">
  <svg class="abs" style="left:0;top:0" width="1200" height="330" viewBox="0 0 1200 330">
    <defs><linearGradient id="ctaBg" x1="0" y1="0" x2="1" y2="0"><stop offset="0" stop-color="#c4780e"/><stop offset=".5" stop-color="#1e1e1e"/><stop offset="1" stop-color="#1e1e1e"/></linearGradient></defs>
    <path d="M0 20C300 0 800 0 1200 20V330H0Z" fill="url(#ctaBg)"/>
  </svg>
  <div class="abs center" style="left:0;width:1200px;top:92px"><span class="eyebrow" style="color:#fff;text-transform:none">Let's Build Something Stronger Together</span></div>
  <h2 class="abs display section-title center" style="left:0;width:1200px;top:146px;color:var(--orange)">Ready to Source High-Performance Composites?</h2>
  <div class="abs" style="left:298px;top:216px;width:455px;height:42px;background:#fff;font-size:10px;color:#999;padding:14px 26px">Email Address</div>
  <a class="abs btn btn-orange" style="left:753px;top:220px">Request a Quote</a>
</section>

<!-- CONTACT BAR -->
<div class="abs" style="left:112px;top:4375px;width:976px;height:66px;background:var(--orange);border-radius:0 0 6px 6px;display:flex;color:#fff;font-size:9px">
  <div style="flex:1;text-align:center;padding-top:10px;border-right:1px solid #fff3"><b style="font-size:11px">Address :</b><br>◉ Unit 12, 480 Harbor Lane,<br>Lakeview 10221</div>
  <div style="flex:1;text-align:center;padding-top:10px;border-right:1px solid #fff3"><b style="font-size:11px">Phone Number :</b><br><br>✆ +1 555 014 2290</div>
  <div style="flex:1;text-align:center;padding-top:10px;border-right:1px solid #fff3"><b style="font-size:11px">Email Id :</b><br><br>✉ info@vorkelsupply.example</div>
  <div style="flex:1;text-align:center;padding-top:10px"><b style="font-size:11px">Website :</b><br><br>◎ URL: www.vorkelsupply.example</div>
</div>

<!-- FOOTER -->
<footer class="section" style="top:4460px;height:336px">
  <div class="abs logo" style="left:45px;top:60px;color:var(--dark)">
    <span class="logo-mark"></span><span class="logo-name">VORKEL</span>
    <span class="logo-sub" style="color:#555">Vantor Omniline Reliant Kinetic Export Lodge</span>
  </div>
  <p class="abs" style="left:52px;top:152px;width:280px;font-size:10px;line-height:19px;color:var(--muted)">Leading North American distributor of high-performance composite fibers, delivering quality, reliability, and innovation across industries.</p>
  <div class="abs foot-col" style="left:346px;top:68px"><h5 style="text-transform:none">Main LINKS</h5><ul><li style="color:var(--orange)">Home</li><li>Our Products</li><li>Our Services</li><li>About Us</li><li>Articles</li><li>Contact Us</li></ul></div>
  <div class="abs foot-col" style="left:513px;top:68px"><h5 style="text-transform:none">Products</h5><ul><li>• Carbon Fiber</li><li>• Aramid Fiber</li><li>• Basalt Fiber</li><li>• High Silica Glass</li><li>• Quartz Fiber</li><li>• Silica Glass</li><li>• Alumina Fiber</li><li>• Vacuum Auxiliary</li></ul></div>
  <div class="abs foot-col" style="left:685px;top:68px"><h5>Industries</h5><ul><li>• Automotive</li><li>• Aerospace</li><li>• Construction</li><li>• Electrical</li><li>• Machinery</li></ul></div>
  <div class="abs foot-col" style="left:853px;top:68px"><h5>Articles</h5><ul><li>• Latest Articles</li><li>• News</li></ul></div>
  <p class="abs" style="left:772px;top:260px;font-size:11px;color:var(--text)">•&nbsp; Advanced Composites Distributor for North America</p>
  <div class="abs center" style="left:0;top:302px;width:1200px;height:34px;background:var(--orange);color:#fff;font-size:10px;line-height:34px">© 2025 VORKEL INC</div>
</footer>

</body>
</html>
```